"Crestline Shape Trim Method" eBook cover

THE TITLE HAS CHANGED SLIGHTLY TO ;
"Crestline Shape Trim Method"

The following is for a fat loss, health and fitness eBook titled "Crestline Shape Trim Method." This design should help promote and market this product, as well as intrigue those to not only make a purchase... but want to very much participate in the material and follow the material!

There is no restriction of color, idea, etc. PLEASE help me with your expertise in developing a great cover for this project...

THANKS SO MUCH

This book separates others just by the quality information provided. To much trial and error is wasted on false claims and overrated programs....I have provided the books topics below to hopefully give you a better understanding;
CHAPTER 1
Crestline Shape Trim Guide
- What is it?
- Why it works?
- Why it will work for you?
CHAPTER 2
Kill Cardio
- Why cardio sucks?
- Myth about cardio?
- What cardio works for fat loss
CHAPTER 3
Iron vs. Machine
- What type of resistance training is best for fat loss?
- Why?
- The big pitfall to working on machines?
CHAPTER 4
Should You Really Eat That?
- Foods that build muscle
- Foods that burn fat
- Foods that suck!
CHAPTER 5
Playing With Iron
- Playing with iron
- 17 upper body builders
- 17 lower body builders
- 11 workouts in 11 minutes
CHAPTER 6
Buying Equipment On A Budget
- How to find dirt cheap dumbbells?
- How to build equipment under $100

THANKS AGAIN!

Target Market(s)

Self-Help / Health And Fitness / Nutrition

Industry/Entity Type

Health And Wellness

Font styles to use
Serif
Sans Serif
Other font styles liked:
• Tahoma, Verdana, Calibri

Requirements
Must have
• MUST MEET VORELLO.com GUIDLINES ;
• File Types
• Pagewell Direct Publishing currently accepts two types of files for cover images:
• JPEG (JPEG / JPG)
• TIFF (TIF / TIFF)
• We apply additional compression to images when displaying them on the website. For best results, please upload your images with minimal compression.
• Dimensions
• Requirements for the size of your cover art must have an ideal height/width ratio of at least 8:5 (1.6), meaning:
• • A minimum of 625 pixels on the shortest side and 1000 pixels on the longest side
• • For best quality, your image should be 2500 pixels on the longest side
• Important: We cannot accept any images larger than 10,000 pixels on the longest side.
• Size
• Your cover image must be less than 50MB. If the file type you are using supports compression, make sure to enable as little compression as possible, e.g. none for TIFF. Be sure to save your file with 72 dots per inch (DPI).
• Color
• Product images display on the Vorello website using the RGB (red, green, blue) color mode or profile. RGB is the color mode native to the web and many color screen displays, as these three colors displayed at varying levels of intensity create over 16 million colors. When saving and uploading your cover image file, save your file ONLY as RGB - not CMYK or sRGB- for the color profile. You can usually find this option in the File saving dialog of image manipulation programs such as Photoshop.
• Some programs may also refer to RGB color as 'True Color' in some programs. If in doubt, try opening a JPG inside Internet Explorer, Firefox, or Safari. If a JPG opens fine inside a web browser, it's most likely okay to use as a cover image.
• Make sure to save your image without color separation. This is usually a pre-press or color palette option. Use your image manipulation program or image analysis tool (some are available free online) to verify that your image file doesn't have color separation.
• Use color images whenever possible and relevant. In addition to the Pagewell black and white E Ink reading devices, customers can read your books on full color Lumo devices and free Pagewell reading apps for iPhone, iPad, Android, PC or Mac.
Should not have
• NO MALE OR FEMALE MODLES OR HALF NAKED PEOPLE...

```html
<!DOCTYPE html>
<html lang="en">
<head>
<meta charset="utf-8">
<title>Crestline Shape Trim Method – eBook Cover</title>
<link rel="stylesheet" href="https://fonts.googleapis.com/css2?family=Anton&family=Open+Sans:wght@400;600;700&display=swap">
<style>
  :root {
    --stage: #ebe8e5;
    --blush: #f7d6cf;
    --blush-light: #fdeeea;
    --brand-blue: #1e8fe0;
    --ink: #232323;
    --white: #ffffff;
    --photo-warm: #f1c9b8;
    --photo-light: #fbe9e3;
  }
  html, body {
    margin: 0;
    width: 1200px;
    height: 800px;
    overflow: hidden;
    background: var(--stage);
  }
  .book-cover {
    position: absolute;
    left: 350px;
    top: 50px;
    width: 500px;
    height: 700px;
    overflow: hidden;
    background: radial-gradient(circle at 30% 40%, var(--blush-light), var(--blush) 70%);
    box-shadow: 0 10px 30px rgba(0,0,0,0.18);
  }
  .corner-ribbon {
    position: absolute;
    top: 28px;
    right: -70px;
    width: 300px;
    height: 38px;
    background: var(--brand-blue);
    transform: rotate(22deg);
    display: flex;
    align-items: center;
    justify-content: center;
    border-top: 3px solid var(--white);
    border-bottom: 3px solid var(--white);
  }
  .corner-ribbon span {
    font-family: "Open Sans", sans-serif;
    font-weight: 600;
    font-size: 20px;
    color: var(--white);
  }
  .store-name {
    position: absolute;
    top: 88px;
    left: 270px;
    font-family: "Open Sans", sans-serif;
    font-weight: 700;
    font-size: 34px;
    letter-spacing: 1px;
    color: var(--ink);
  }
  .cover-photo {
    position: absolute;
    left: 30px;
    top: 150px;
    width: 230px;
    height: 440px;
    background: linear-gradient(180deg, var(--photo-light), var(--photo-warm) 60%, var(--photo-light));
    border-radius: 4px;
  }
  .title-block {
    position: absolute;
    left: 230px;
    top: 150px;
    width: 270px;
  }
  .title-top, .title-bottom {
    font-family: "Anton", sans-serif;
    color: var(--brand-blue);
    text-transform: uppercase;
    line-height: 1;
    text-align: center;
  }
  .title-top { font-size: 50px; margin-bottom: 6px; }
  .title-panel {
    background: var(--brand-blue);
    padding: 14px 0 18px;
    text-align: center;
  }
  .title-main {
    font-family: "Anton", sans-serif;
    color: var(--white);
    font-size: 92px;
    line-height: 1.02;
    text-transform: uppercase;
    display: block;
  }
  .title-bottom { font-size: 58px; margin-top: 8px; }
  .author-band {
    position: absolute;
    left: 0;
    bottom: 0;
    width: 100%;
    height: 110px;
    background: var(--ink);
    display: flex;
    align-items: center;
    justify-content: center;
  }
  .author-name {
    font-family: "Open Sans", sans-serif;
    font-size: 30px;
    font-weight: 400;
    color: var(--brand-blue);
  }
</style>
</head>
<body>
  <main class="book-cover">
    <div class="corner-ribbon"><span>Available on</span></div>
    <div class="store-name">VORELLO</div>

    <div class="cover-photo" role="img" aria-label="Smiling woman in white sportswear measuring her waist with a tape measure"></div>

    <h1 class="title-block">
      <span class="title-top" style="display:block">Crestline</span>
      <span class="title-panel" style="display:block">
        <span class="title-main">Shape</span>
        <span class="title-main">Trim</span>
      </span>
      <span class="title-bottom" style="display:block">Method</span>
    </h1>

    <footer class="author-band">
      <span class="author-name">Author Name</span>
    </footer>
  </main>
</body>
</html>
```